glow 742 is renewing its image

more dynamic website, make it look more attractive for the services we offer, at the same time more accurate on the services description. We want people to know we offer treatments that big corporations offer but not as expensive as they offer it. prices will be add by me once the website is approve
Updates

already have a website with wix.com www.glow742dermis.com

Target Market(s)

women between 21 to 75

Industry/Entity Type

beauty services, body contouring

Colors

Designer to choose colors to be used in the design.

Requirements
Must have
• pictures of treatments
Nice to have
• accurate information about treatmnets, treatments menu
Should not have
• no online shopping

```html
<!DOCTYPE html>
<html lang="en">
<head>
<meta charset="utf-8">
<title>Glow 742 Skin Lounge</title>
<link href="https://fonts.googleapis.com/css2?family=Libre+Caslon+Text:wght@400;700&family=Great+Vibes&family=Poppins:wght@300;400;500;600&display=swap" rel="stylesheet">
<style>
:root{
  --brown:#a8703f;
  --tan:#c99460;
  --tan-soft:#e8cfb3;
  --cream:#f6ede4;
  --ink:#1c1714;
  --body:#6b5c50;
  --dark:#262220;
  --white:#ffffff;
}
*{margin:0;padding:0;box-sizing:border-box}
html,body{width:1200px;height:4471px;overflow:hidden;background:var(--white)}
body{position:relative;font-family:"Poppins",sans-serif;color:var(--ink)}
.abs{position:absolute}
.photo{position:absolute}
.serif{font-family:"Libre Caslon Text",serif;font-weight:700}
.script{font-family:"Great Vibes",cursive;font-weight:400}
.eyebrow{font-family:"Great Vibes",cursive;font-size:24px;color:var(--brown)}
.btn{position:absolute;display:inline-block;background:var(--tan);color:var(--white);font-size:13px;font-weight:500;letter-spacing:.5px;padding:0 24px;height:38px;line-height:38px}
.btn::after{content:"";position:absolute;left:6px;top:6px;right:-6px;bottom:-6px;border:1px solid var(--tan);z-index:-1}

/* header */
.brand{position:absolute;left:60px;top:14px;font-family:"Libre Caslon Text",serif;font-size:40px;color:var(--brown);font-weight:400}
.brand small{display:block;font-family:"Poppins",sans-serif;font-size:12px;margin:-6px 0 0 46px}
.nav{position:absolute;left:364px;top:30px;display:flex;gap:26px;font-size:12px;font-weight:500}
.nav .on{color:var(--brown)}
.phone{position:absolute;left:992px;top:24px;font-size:15px;color:var(--brown);font-style:italic;display:flex;align-items:center;gap:8px}
.rule{position:absolute;left:60px;top:75px;width:1080px;height:1px;background:#e6d8cb}

/* hero */
.hero-script{left:208px;top:140px;font-size:92px;color:var(--brown)}
.hero-title{left:306px;top:268px;font-size:44px;line-height:52px}
.play{position:absolute;left:472px;top:393px;display:flex;align-items:center;gap:12px;font-size:13px;font-weight:500}
.play span{width:40px;height:40px;border:1px solid var(--ink);border-radius:50%;display:flex;align-items:center;justify-content:center}

/* welcome band */
.welcome{left:0;top:691px;width:1200px;height:504px;background:var(--brown)}
.welcome-frame{left:168px;top:782px;width:831px;height:312px;border:2px solid var(--tan-soft)}
.welcome-text{left:330px;top:830px;width:540px;text-align:center;color:var(--white)}
.welcome-text .eyebrow{color:var(--white);font-size:26px}
.welcome-text h2{font-size:32px;margin:6px 0 18px}
.welcome-text p{font-size:12px;line-height:20px;font-style:italic;font-weight:300}

/* treatments */
.sec-head{left:0;width:1200px;text-align:center}
.sec-head h2{font-size:32px}
.card{position:absolute;width:240px}
.card h3{font-size:15px;text-align:center;line-height:24px}
.card .plate{position:absolute;left:0;width:240px;background:#000;color:var(--white);text-align:center;padding:16px 18px}
.plate h4{font-family:"Libre Caslon Text",serif;font-size:15px;margin-bottom:10px}
.plate p{font-size:11px;line-height:19px}
.dots{left:572px;top:1770px;display:flex;gap:6px}
.dots i{display:block;height:4px;width:34px;background:var(--brown)}
.dots i+i{width:18px;background:#ddd}

/* post surgery */
.post-panel{left:466px;top:1860px;width:734px;height:433px;background:var(--tan)}
.post-text{left:639px;top:1920px;width:400px;color:var(--white)}
.post-text .eyebrow{color:var(--white)}
.post-text h2{font-size:32px;margin:2px 0 18px}
.post-text .lead{font-size:14px;line-height:22px;margin-bottom:16px}
.post-text p{font-size:11.5px;line-height:20px;margin-bottom:6px}

/* why */
.why{left:737px;top:2465px}
.why h2{font-size:32px;line-height:41px}

/* subscribe */
.sub{left:0;top:2753px;width:1200px;height:443px;background:linear-gradient(90deg,#d9b58f 0%,#e9d3bb 55%,#d7b289 100%)}
.sub-text{left:61px;top:2845px}
.sub-text h2{font-size:32px;line-height:41px;width:640px}
.field{position:absolute;left:61px;width:295px;height:35px;border:1px solid var(--white);color:var(--white);font-size:12px;padding:9px 10px}
.sub-btn{left:61px;top:3072px;background:var(--brown)}
.sub-btn::after{border-color:var(--brown)}

/* about */
.about{left:492px;top:3318px}
.about h2{font-size:32px;line-height:42px}
.about-copy{left:135px;top:3682px;width:360px;font-size:11.5px;line-height:20px;color:var(--body)}
.about-copy p+p{margin-top:10px}

/* feed */
.feed-label{left:506px;top:4018px;width:188px;height:62px;background:var(--white);display:flex;align-items:center;justify-content:center;gap:10px;font-size:18px;font-weight:500}

/* footer */
.footer{left:0;top:4143px;width:1200px;height:295px;background:var(--dark);color:#d9d0c8}
.foot-brand{left:60px;top:4215px;font-family:"Libre Caslon Text",serif;font-size:42px;color:var(--brown)}
.foot-brand small{display:block;font-family:"Poppins",sans-serif;font-size:13px;margin:-8px 0 0 46px}
.social{position:absolute;top:4305px;width:32px;height:32px;border-radius:50%;background:var(--white)}
.foot-col{position:absolute;top:4210px;font-size:12px;line-height:26px}
.foot-col h4{font-family:"Libre Caslon Text",serif;font-size:18px;color:var(--brown);font-weight:700;margin-bottom:8px}
.contact-row{display:flex;gap:14px;align-items:flex-start;line-height:20px;margin-bottom:18px}
.foot-col u{display:block;line-height:20px}
.copy{left:0;top:4438px;width:1200px;height:33px;background:var(--tan);color:var(--white);text-align:center;font-size:11px;line-height:33px}
</style>
</head>
<body>

<!-- header -->
<div class="brand">Glow 742<small>Skin Lounge</small></div>
<nav class="nav"><span class="on">HOME</span><span>TREATMENTS</span><span>BEST SURGERY TREATMENT</span><span>CONTACT US</span><span>ABOUT US</span><span>MORE</span></nav>
<div class="phone"><svg width="18" height="18" viewBox="0 0 24 24"><path fill="#a8703f" d="M6.6 10.8a15 15 0 0 0 6.6 6.6l2.2-2.2c.3-.3.7-.4 1-.2 1.1.4 2.3.6 3.6.6.6 0 1 .4 1 1V20c0 .6-.4 1-1 1C10.6 21 3 13.4 3 4c0-.6.4-1 1-1h3.5c.6 0 1 .4 1 1 0 1.3.2 2.5.6 3.6.1.3 0 .7-.2 1z"/></svg>(555) 214-3380</div>
<div class="rule"></div>

<!-- hero -->
<div class="photo" role="img" aria-label="Faded portrait of a woman in soft light" style="left:0;top:86px;width:226px;height:150px;background:linear-gradient(135deg,#f4ece6,#fbf7f4)"></div>
<div class="photo" role="img" aria-label="Facial mask treatment being applied" style="left:0;top:248px;width:240px;height:255px;background:linear-gradient(135deg,#e4c9b5,#bfa08c)"></div>
<div class="photo" role="img" aria-label="Woman relaxing on a spa bed" style="left:0;top:538px;width:229px;height:152px;background:linear-gradient(135deg,#f0dfd2,#c99a7c)"></div>
<div class="photo" role="img" aria-label="Face massage at the spa" style="left:731px;top:90px;width:262px;height:172px;background:linear-gradient(135deg,#6e4a35,#d4a98a)"></div>
<div class="photo" role="img" aria-label="Microdermabrasion device on a client's face" style="left:938px;top:351px;width:262px;height:314px;background:linear-gradient(135deg,#e9dfdc,#b9c3cc)"></div>
<div class="photo" role="img" aria-label="Wooden roller massage on legs" style="left:377px;top:481px;width:374px;height:210px;background:linear-gradient(135deg,#efe2d6,#c89a6c)"></div>
<div class="abs script hero-script">Glow 742</div>
<h1 class="abs serif hero-title">Skin Lounge and Post<br>Liposuction Care</h1>
<span class="btn" style="left:304px;top:395px">LEARN MORE</span>
<div class="play"><span><svg width="10" height="12" viewBox="0 0 10 12"><path d="M0 0l10 6-10 6z" fill="#1c1714"/></svg></span>PLAY VIDEO</div>

<!-- welcome band -->
<div class="abs welcome"></div>
<div class="abs welcome-frame"></div>
<div class="photo" role="img" aria-label="Woman's back wrapped in a towel with spa stones" style="left:921px;top:747px;width:278px;height:365px;background:linear-gradient(180deg,#c99a74,#f1e4d8)"></div>
<div class="abs welcome-text">
  <div class="eyebrow">Welcome to Glow 742</div>
  <h2 class="serif">Skin Lounge and Post Liposuction Care</h2>
  <p>Located in Fairbridge, CT. Glow 742 Skin Lounge makes the most of what you've got with services designed to complement your looks and needs. We feature an extensive list of treatments, including natural peels, tripolar radio frequency, microdermabrasion, facial and body microcurrent, post operatory Treatment, wood therapy, ultrasound body sculpting, complete facial treatment packages, vacuum therapy and much more!</p>
</div>
<svg class="abs" style="left:0;top:1180px" width="1200" height="16" viewBox="0 0 1200 16" preserveAspectRatio="none"><path fill="#fff" d="M0 16 L0 4 L12 16 L24 4 L36 16 L48 4 L60 16 L72 4 L84 16 L96 4 L108 16 L120 4 L132 16 L144 4 L156 16 L168 4 L180 16 L192 4 L204 16 L216 4 L228 16 L240 4 L252 16 L264 4 L276 16 L288 4 L300 16 L312 4 L324 16 L336 4 L348 16 L360 4 L372 16 L384 4 L396 16 L408 4 L420 16 L432 4 L444 16 L456 4 L468 16 L480 4 L492 16 L504 4 L516 16 L528 4 L540 16 L552 4 L564 16 L576 4 L588 16 L600 4 L612 16 L624 4 L636 16 L648 4 L660 16 L672 4 L684 16 L696 4 L708 16 L720 4 L732 16 L744 4 L756 16 L768 4 L780 16 L792 4 L804 16 L816 4 L828 16 L840 4 L852 16 L864 4 L876 16 L888 4 L900 16 L912 4 L924 16 L936 4 L948 16 L960 4 L972 16 L984 4 L996 16 L1008 4 L1020 16 L1032 4 L1044 16 L1056 4 L1068 16 L1080 4 L1092 16 L1104 4 L1116 16 L1128 4 L1140 16 L1152 4 L1164 16 L1176 4 L1188 16 L1200 4 L1200 16Z"/></svg>

<!-- treatments -->
<div class="abs sec-head" style="top:1282px"><div class="eyebrow">What We Do</div><h2 class="serif">Our Treatments</h2></div>

<div class="card" style="left:75px;top:1397px">
  <div role="img" aria-label="Green clay facial peel treatment" style="height:298px;background:linear-gradient(135deg,#8fa08f,#e5dcd2)"></div>
  <h3 class="serif" style="margin-top:14px">Maximum Glow 742 Natural<br>Peel</h3>
</div>
<div class="card" style="left:346px;top:1388px">
  <h3 class="serif">Post-surgery<br>Treatment</h3>
  <div role="img" aria-label="Therapist performing a post-surgery treatment" style="height:298px;margin-top:10px;background:linear-gradient(135deg,#c9d7de,#d9b9a3)"></div>
</div>
<div class="card" style="left:615px;top:1397px">
  <div role="img" aria-label="Ultrasound cavitation device on a leg" style="height:166px;background:linear-gradient(135deg,#e6e2df,#c9b2a1)"></div>
  <div class="plate" style="top:166px;height:132px"><h4>$79 Per Person</h4><p>Body sculpting treatment with no anesthesia, no scars, no discomfort, no down-time and presents a risk-free alternative to liposuction.</p></div>
  <h3 class="serif" style="margin-top:146px">Ultrasound<br>Cavitation</h3>
</div>
<div class="card" style="left:884px;top:1388px">
  <h3 class="serif">Diamond<br>Microdermoabrasion</h3>
  <div role="img" aria-label="Diamond microdermabrasion on a client's face" style="height:298px;margin-top:10px;background:linear-gradient(135deg,#e3e0dd,#c7a592)"></div>
</div>
<div class="abs dots"><i></i><i></i></div>

<!-- post surgery -->
<div class="abs post-panel"></div>
<svg class="abs" style="left:596px;top:2281px" width="604" height="14" viewBox="0 0 604 14" preserveAspectRatio="none"><path fill="#fff" d="M0 14 L0 0 L12 14 L24 0 L36 14 L48 0 L60 14 L72 0 L84 14 L96 0 L108 14 L120 0 L132 14 L144 0 L156 14 L168 0 L180 14 L192 0 L204 14 L216 0 L228 14 L240 0 L252 14 L264 0 L276 14 L288 0 L300 14 L312 0 L324 14 L336 0 L348 14 L360 0 L372 14 L384 0 L396 14 L408 0 L420 14 L432 0 L444 14 L456 0 L468 14 L480 0 L492 14 L504 0 L516 14 L528 0 L540 14 L552 0 L564 14 L576 0 L588 14 L604 0 L604 14Z"/></svg>
<div class="photo" role="img" aria-label="Facial microcurrent treatment with probes" style="left:61px;top:1860px;width:337px;height:240px;background:linear-gradient(135deg,#e8e6e6,#caa58d)"></div>
<div class="photo" role="img" aria-label="Radio frequency device on the abdomen" style="left:259px;top:2123px;width:337px;height:262px;background:linear-gradient(135deg,#c9d9e2,#e6cbbb)"></div>
<div class="abs post-text">
  <div class="eyebrow">What We Do</div>
  <h2 class="serif">Post-surgery Treatment</h2>
  <div class="lead">Post Surgery, Pre &amp; Post Liposuction, Tummy Tuck, Mammoplasty, Neck Lift, Breast Implant)</div>
  <p>The post-surgery treatment is a combination of techniques that speed up the patient's healing process after surgery. Its main objective is to eliminate the surgery's inflammation and correct the skin irregularities produced by Fibrosis.</p>
  <p>Fibrosis is an effect suffered by most patients after surgery. If the patient notices hardening of the skin tissues, lumps or deformations in the area that was subjected to surgery, then there is Fibrosis and post-surgery treatment is then needed.</p>
</div>

<!-- why -->
<div class="photo" role="img" aria-label="Smiling woman on a massage table with orchids and stones" style="left:0;top:2397px;width:617px;height:356px;background:linear-gradient(90deg,#f3ece6,#e9d4c3 60%,#fff)"></div>
<div class="abs why"><div class="eyebrow">Why We</div><h2 class="serif">Complete Body and Facial<br>Treatments with 100%<br>Natural Products</h2></div>
<span class="btn" style="left:737px;top:2637px">CONTACT US</span>

<!-- subscribe -->
<div class="abs sub" role="img" aria-label="Spa still life with towels, candles, stones and oil"></div>
<div class="abs sub-text"><div class="eyebrow">Exclusive deals and discounts.</div><h2 class="serif">Get 10% off your first treatment when you subscribe!</h2></div>
<div class="field" style="top:2967px">Name :</div>
<div class="field" style="top:3014px">Email :</div>
<span class="btn sub-btn">SUBSRIBE NOW</span>
<svg class="abs" style="left:0;top:3182px" width="1200" height="14" viewBox="0 0 1200 14" preserveAspectRatio="none"><path fill="#fff" d="M0 14 L0 2 L12 14 L24 2 L36 14 L48 2 L60 14 L72 2 L84 14 L96 2 L108 14 L120 2 L132 14 L144 2 L156 14 L168 2 L180 14 L192 2 L204 14 L216 2 L228 14 L240 2 L252 14 L264 2 L276 14 L288 2 L300 14 L312 2 L324 14 L336 2 L348 14 L360 2 L372 14 L384 2 L396 14 L408 2 L420 14 L432 2 L444 14 L456 2 L468 14 L480 2 L492 14 L504 2 L516 14 L528 2 L540 14 L552 2 L564 14 L576 2 L588 14 L600 2 L612 14 L624 2 L636 14 L648 2 L660 14 L672 2 L684 14 L696 2 L708 14 L720 2 L732 14 L744 2 L756 14 L768 2 L780 14 L792 2 L804 14 L816 2 L828 14 L840 2 L852 14 L864 2 L876 14 L888 2 L900 14 L912 2 L924 14 L936 2 L948 14 L960 2 L972 14 L984 2 L996 14 L1008 2 L1020 14 L1032 2 L1044 14 L1056 2 L1068 14 L1080 2 L1092 14 L1104 2 L1116 14 L1128 2 L1140 14 L1152 2 L1164 14 L1176 2 L1188 14 L1200 2 L1200 14Z"/></svg>

<!-- about -->
<div class="photo" role="img" aria-label="Relaxing head massage with pink flowers" style="left:135px;top:3318px;width:299px;height:339px;background:linear-gradient(135deg,#d9c2b3,#f3e8e1)"></div>
<div class="abs about"><div class="eyebrow">About Us</div><h2 class="serif">You deserve more, whether<br>it's a suite of services</h2></div>
<span class="btn" style="left:494px;top:3440px">ABOUT MORE</span>
<div class="photo" role="img" aria-label="Facial treatment with a blue headband" style="left:577px;top:3552px;width:261px;height:321px;background:linear-gradient(135deg,#e4e2e2,#8fb2c4)"></div>
<div class="photo" role="img" aria-label="Skin device facial treatment" style="left:670px;top:3436px;width:337px;height:226px;background:linear-gradient(135deg,#c2866a,#e9cdbb)"></div>
<div class="abs about-copy">
  <p>You deserve more, whether it's a suite of services that treats every bodily need, a top-notch professional staff or a relaxing venue to enjoy them in. This is where We shine.</p>
  <p>Here, you can take your pick of from a variety of beauty-boosting services. We use Peruvian natural products. For instance, the Skin Care Body Wraps, which are tailored to relax the body, detoxify, exfoliate and hydrate the skin, all while helping you to lose inches. This treatments enhances both your psychological and physical wellness.</p>
</div>

<!-- feed strip -->
<div class="photo" role="img" aria-label="Treatment room photo" style="left:0;top:3955px;width:196px;height:188px;background:linear-gradient(135deg,#cfa88e,#8f6a55)"></div>
<div class="photo" role="img" aria-label="Wood therapy roller photo" style="left:201px;top:3955px;width:196px;height:188px;background:linear-gradient(135deg,#e7d3c0,#b98c63)"></div>
<div class="photo" role="img" aria-label="Facial peel photo" style="left:402px;top:3955px;width:196px;height:188px;background:linear-gradient(135deg,#f0d7c6,#c89f88)"></div>
<div class="photo" role="img" aria-label="Face massage photo" style="left:603px;top:3955px;width:196px;height:188px;background:linear-gradient(135deg,#ddc6b8,#8f7a70)"></div>
<div class="photo" role="img" aria-label="Skin device treatment photo" style="left:804px;top:3955px;width:196px;height:188px;background:linear-gradient(135deg,#e3dfdc,#b8a194)"></div>
<div class="photo" role="img" aria-label="Massage tools photo" style="left:1005px;top:3955px;width:195px;height:188px;background:linear-gradient(135deg,#efe6dc,#c9a57f)"></div>
<div class="abs feed-label"><svg width="22" height="22" viewBox="0 0 22 22"><rect x="2" y="2" width="18" height="18" fill="none" stroke="#a8703f" stroke-width="2"/></svg>PHOTO FEED</div>

<!-- footer -->
<div class="abs footer"></div>
<div class="abs foot-brand">Glow 742<small>Skin Lounge</small></div>
<span class="social" style="left:60px"></span><span class="social" style="left:106px"></span>
<div class="foot-col" style="left:338px"><h4>Sitemap</h4><div>- Home</div><div>- Treatments</div><div>- Post Surgery Treatment</div><div>- Contact Us</div><div>- About Us</div></div>
<div class="foot-col" style="left:613px">
  <h4>Contact Us</h4>
  <div class="contact-row"><svg width="18" height="20" viewBox="0 0 18 20"><path d="M9 1a6 6 0 0 0-6 6c0 5 6 12 6 12s6-7 6-12a6 6 0 0 0-6-6z" fill="none" stroke="#c99460" stroke-width="1.6"/><circle cx="9" cy="7" r="2" fill="#c99460"/></svg><span>18 Alder Row Fairbridge<br>CT 06999</span></div>
  <div class="contact-row"><svg width="20" height="16" viewBox="0 0 20 16"><rect x="1" y="1" width="18" height="14" fill="none" stroke="#c99460" stroke-width="1.6"/><path d="M1 1l9 8 9-8" fill="none" stroke="#c99460" stroke-width="1.6"/></svg><span>glow742spa@mailbox.com</span></div>
  <div class="contact-row"><svg width="18" height="18" viewBox="0 0 24 24"><path fill="none" stroke="#c99460" stroke-width="2" d="M6.6 10.8a15 15 0 0 0 6.6 6.6l2.2-2.2c.3-.3.7-.4 1-.2 1.1.4 2.3.6 3.6.6.6 0 1 .4 1 1V20c0 .6-.4 1-1 1C10.6 21 3 13.4 3 4c0-.6.4-1 1-1h3.5c.6 0 1 .4 1 1 0 1.3.2 2.5.6 3.6.1.3 0 .7-.2 1z"/></svg><span>(555) 214-3380 or<br>(555) 214-3391</span></div>
</div>
<div class="foot-col" style="left:888px;width:230px">
  <h4>Policy</h4>
  <u>Reservation Fee and<br>Cancellation Policy</u>
  <div style="line-height:20px;margin-top:8px">To schedule your appointment have your DealDrop voucher # ready to secure your date and time.</div>
</div>
<div class="abs copy">© 2021 Glow 742 Skin Lounge- All Right Reserved.</div>

</body>
</html>
```